Business Card Design

We are a commercial real estate brokerage in San Francisco, leasing office buildings downtown.
I would like a clean, elegant look. Simple but powerful .

Industry/Entity Type

Business

Contact Information for Business Card

Colin Farrow
lic# 07281549
415.555.0172
colin@tarvo-commercial.example
tarvo-commercial.example

```html
<!DOCTYPE html>
<html lang="en">
<head>
<meta charset="utf-8">
<title>Tarvo Commercial — Business Card</title>
<link rel="stylesheet" href="https://fonts.googleapis.com/css2?family=PT+Sans:wght@400;700&display=swap">
<style>
  :root {
    --page-bg: #e6dcc6;
    --card-dark: #2c2c2c;
    --card-light: #ffffff;
    --skyline: #474747;
    --text-light: #f2f2f2;
    --brand-slate: #6f7c92;
  }
  * { box-sizing: border-box; margin: 0; padding: 0; }
  html, body {
    width: 1200px;
    height: 510px;
    overflow: hidden;
    background: var(--page-bg);
    font-family: "PT Sans", sans-serif;
  }
  .card {
    position: absolute;
    left: 375px;
    top: 116px;
    width: 418px;
    height: 244px;
    border-radius: 14px;
    overflow: hidden;
    background: var(--card-dark);
    display: flex;
  }
  .brand-panel {
    width: 115px;
    height: 100%;
    background: var(--card-light);
    position: relative;
  }
  .brand-lockup {
    position: absolute;
    left: 40px;
    top: 56px;
    height: 130px;
    display: flex;
    flex-direction: column;
    align-items: center;
    justify-content: center;
    gap: 10px;
  }
  .brand-name {
    writing-mode: vertical-rl;
    transform: rotate(180deg);
    font-size: 17px;
    font-weight: 700;
    letter-spacing: 1px;
    text-transform: uppercase;
    color: var(--brand-slate);
    white-space: nowrap;
    line-height: 1;
  }
  .brand-mark {
    width: 12px;
    height: 12px;
    background: var(--brand-slate);
  }
  .contact-panel {
    flex: 1;
    position: relative;
  }
  .contact {
    position: absolute;
    left: 88px;
    top: 85px;
    color: var(--text-light);
  }
  .contact-name {
    font-size: 13.5px;
    font-weight: 400;
    margin-bottom: 9px;
  }
  .contact-line {
    font-size: 10.5px;
    line-height: 15.5px;
    letter-spacing: 0.2px;
  }
  .skyline {
    position: absolute;
    left: 0;
    right: 0;
    bottom: 0;
    height: 36px;
    background: linear-gradient(to bottom, rgba(71,71,71,0) 0%, var(--skyline) 45%, var(--skyline) 100%);
  }
</style>
</head>
<body>
  <div class="card">
    <div class="brand-panel">
      <div class="brand-lockup">
        <span class="brand-name">Tarvo Commercial</span>
        <span class="brand-mark"></span>
      </div>
    </div>
    <div class="contact-panel">
      <div class="contact">
        <p class="contact-name">Colin Farrow</p>
        <p class="contact-line">lic# 07281549</p>
        <p class="contact-line">415.555.0172</p>
        <p class="contact-line">colin@tarvo-commercial.example</p>
        <p class="contact-line">tarvo-commercial.example</p>
      </div>
      <div class="skyline" role="img" aria-label="Grey silhouette of the downtown San Francisco skyline along the bottom edge"></div>
    </div>
  </div>
</body>
</html>
```